Modern Lawfirm Business Card Design

We're looking for a business card to incorporate the newly created logo we had made.

Ideally looking for a law firm business card demonstrating, modern, minimalist, strong/bold design.

I'm open to any design honestly, but nothing "flashy".

Target Market(s)

Immigration law, family immigration, humanitarian, general legal

Industry/Entity Type

Law Firm

Contact Information for Business Card

Please use dummy information, name, street address, city, state, phone number, email, website.

Font styles to use
Serif
Sans Serif

Requirements
Must have
• Please use dummy information, name, street address, city, state, phone number, email, website.

```html
<!DOCTYPE html>
<html lang="en">
<head>
<meta charset="utf-8">
<title>Castellan Law — Business Card</title>
<link rel="stylesheet" href="https://fonts.googleapis.com/css2?family=Cinzel:wght@600&family=Montserrat:wght@400;600&display=swap">
<style>
  :root {
    --brand-blue: #2d66a8;
    --brand-blue-dark: #275a95;
    --paper: #f7f8fa;
    --rule: #e4e7ec;
    --ink-muted: #8a8f98;
    --ink-dark: #3b3f45;
    --white: #ffffff;
    --backdrop: #4a4a4c;
  }
  * { box-sizing: border-box; margin: 0; padding: 0; }
  html, body { width: 1200px; height: 946px; overflow: hidden; }
  body {
    background: var(--backdrop);
    font-family: "Montserrat", Arial, sans-serif;
    display: flex;
    flex-direction: column;
    align-items: center;
    justify-content: center;
    gap: 60px;
  }
  .card {
    position: relative;
    width: 700px;
    height: 400px;
    background: var(--paper);
    overflow: hidden;
    box-shadow: 0 14px 30px rgba(0,0,0,.45);
  }

  /* Front */
  .front-band {
    position: absolute; left: 0; top: 0; right: 0; height: 190px;
    background: var(--brand-blue);
  }
  .front-name {
    position: absolute; left: 50px; top: 108px;
    font-family: "Cinzel", Georgia, serif; font-weight: 600;
    font-size: 60px; line-height: 1; letter-spacing: 2px; color: var(--white);
    white-space: nowrap;
  }
  .front-frame {
    position: absolute; left: 40px; right: 40px; top: 220px; bottom: 40px;
    border: 1px solid var(--rule);
  }
  .front-web {
    position: absolute; left: 0; right: 0; top: 300px; text-align: center;
    font-size: 15px; letter-spacing: 6px; color: var(--ink-muted);
  }

  /* Back */
  .back-top {
    position: absolute; left: 0; top: 0; right: 0; height: 150px;
    background: var(--paper);
  }
  .holder {
    position: absolute; right: 40px; top: 34px; text-align right;
    text-align: right;
    border-right: 2px solid var(--brand-blue); padding-right: 10px;
  }
  .holder-name { font-size: 20px; font-weight: 600; color: var(--brand-blue); }
  .holder-role { font-size: 12px; color: var(--ink-dark); }
  .back-body {
    position: absolute; left: 0; right: 0; top: 150px; bottom: 0;
    background: var(--brand-blue);
  }
  .back-logo-box {
    position: absolute; left: 0; top: 100px; width: 350px; height: 80px;
    background: var(--brand-blue);
    display: flex; align-items: center; padding-left: 28px;
    z-index: 2;
  }
  .back-logo-name {
    font-family: "Cinzel", Georgia, serif; font-weight: 600;
    font-size: 30px; line-height: 1; letter-spacing: 1px; color: var(--white);
    white-space: nowrap;
  }
  .emblem-area {
    position: absolute; left: 170px; top: 205px; width: 200px; height: 165px;
    background: var(--brand-blue-dark); border-radius: 12px;
  }
  .contact-list {
    position: absolute; left: 400px; top: 185px; list-style: none;
    display: flex; flex-direction: column; gap: 14px;
  }
  .contact-item {
    display: flex; align-items: center; gap: 12px;
    color: var(--white); font-size: 14px; line-height: 1.25;
  }
  .contact-icon { width: 24px; height: 24px; flex: none; }
</style>
</head>
<body>

  <section class="card card-front">
    <div class="front-band"></div>
    <div class="front-name">CASTELLAN LAW</div>
    <div class="front-frame"></div>
    <div class="front-web">www.yourwebsitehere.com</div>
  </section>

  <section class="card card-back">
    <div class="back-top"></div>
    <div class="holder">
      <div class="holder-name">Your Name Here</div>
      <div class="holder-role">Designation</div>
    </div>
    <div class="back-body"></div>
    <div class="back-logo-box"><span class="back-logo-name">CASTELLAN LAW</span></div>
    <div class="emblem-area" role="img" aria-label="Faint scales of justice emblem"></div>
    <ul class="contact-list">
      <li class="contact-item">
        <svg class="contact-icon" viewBox="0 0 24 24" fill="none" stroke="#fff" stroke-width="1.6"><circle cx="12" cy="12" r="10.5"/><rect x="6.5" y="8" width="11" height="8"/><path d="M6.5 8l5.5 4.5L17.5 8"/></svg>
        <span>info@yourwebsitehere.com</span>
      </li>
      <li class="contact-item">
        <svg class="contact-icon" viewBox="0 0 24 24" fill="none" stroke="#fff" stroke-width="1.6"><circle cx="12" cy="12" r="10.5"/><path d="M8.5 7.5l2 2-1.2 1.5a7 7 0 003.7 3.7l1.5-1.2 2 2-1.5 1.5c-4 0-8-4-8-8z"/></svg>
        <span>+00 (0)123 456789</span>
      </li>
      <li class="contact-item">
        <svg class="contact-icon" viewBox="0 0 24 24" fill="none" stroke="#fff" stroke-width="1.6"><circle cx="12" cy="12" r="10.5"/><path d="M6.5 12L12 7l5.5 5M8.5 11v6h7v-6"/></svg>
        <span>Lorem middle park, ipsum<br>Street name, (0123 456)</span>
      </li>
      <li class="contact-item">
        <svg class="contact-icon" viewBox="0 0 24 24" fill="none" stroke="#fff" stroke-width="1.6"><circle cx="12" cy="12" r="10.5"/><circle cx="12" cy="12" r="5.5"/><path d="M6.5 12h11M12 6.5c2 2 2 9 0 11M12 6.5c-2 2-2 9 0 11"/></svg>
        <span>www.yourwebsitehere.com</span>
      </li>
    </ul>
  </section>

</body>
</html>
```